Dental practice logo either "Molarbrook by Craft" or "Dental Lumora Clinic"

Dental practice with either of the logos mentioned above as we haven't decided on the name depends on which one looks better. Our motto of the practice is to create beautiful smiles and perform general dentistry.
Dr Oswin Halvereth
47 Tallowmere Road
Wrenfield
Northvale 4920 and also the contact number, email address and website.
On the backside of the card it should be about the next appointment and also mention on the bottom" If unable to keep an appointment kindly give 24 hours notice otherwise a fee will be charged for the time reserved.
Reason: As it may take longer to design
We want the business card only on the dental practice named Dental Lumora Clinic and with a caption underneath the practice name as "Harrowgate's home of dentistry"
Target Market(s)
dental patients and general population who want beautiful smile
Industry/Entity Type
Dental
Look and feel

```html
<!DOCTYPE html>
<html lang="en">
<head>
<meta charset="utf-8">
<title>Dental Lumora Clinic – Business Card</title>
<link href="https://fonts.googleapis.com/css2?family=Poppins:wght@400;500;600;700&display=swap" rel="stylesheet">
<style>
  :root {
    --ink: #2f4f84;
    --ink-soft: #4b6a9c;
    --sky: #8db5dd;
    --sky-light: #dce9f6;
    --paper: #ffffff;
    --backdrop: #e6e8ec;
    --skin: #e9c3ad;
    --skin-light: #f6e3d8;
    --line: #3d5a8c;
  }
  * { box-sizing: border-box; margin: 0; padding: 0; }
  html, body { width: 1200px; height: 720px; overflow: hidden; }
  body {
    background: var(--backdrop);
    font-family: "Poppins", sans-serif;
    color: var(--ink);
    display: flex;
    align-items: center;
    justify-content: center;
    gap: 40px;
  }
  .card {
    width: 540px;
    height: 309px;
    position: relative;
    overflow: hidden;
    background: var(--paper);
    box-shadow: 0 10px 30px rgba(30, 40, 60, 0.18);
  }

  /* Front */
  .card-front {
    background: linear-gradient(115deg, var(--sky) 0%, var(--sky-light) 42%, var(--paper) 62%);
  }
  .smile-photo {
    position: absolute;
    top: 0; right: 0;
    width: 48%;
    height: 100%;
    background: linear-gradient(100deg, rgba(246,227,216,0) 0%, rgba(246,227,216,0.7) 22%, var(--skin-light) 38%, var(--skin) 75%, #d9a991 100%);
  }
  .front-content {
    position: absolute;
    top: 28px;
    left: 30px;
    width: 330px;
  }
  .brand {
    display: flex;
    align-items: center;
    gap: 10px;
  }
  .brand-dot {
    width: 14px; height: 14px;
    border-radius: 50%;
    background: var(--ink);
  }
  .brand-name {
    font-size: 25px;
    font-weight: 600;
    letter-spacing: 0.2px;
    line-height: 1.1;
  }
  .tagline {
    font-size: 12.5px;
    margin: 4px 0 0 24px;
    color: var(--ink-soft);
    letter-spacing: 0.3px;
  }
  .doctor {
    margin-top: 22px;
    font-size: 16px;
    font-weight: 600;
  }
  .contact-list { list-style: none; margin-top: 6px; }
  .contact-list li {
    display: flex;
    align-items: flex-start;
    gap: 8px;
    font-size: 13.5px;
    line-height: 1.5;
  }
  .contact-list svg { width: 12px; height: 12px; margin-top: 4px; flex: none; fill: var(--ink); }
  .contact-list .email,
  .contact-list .address { font-weight: 600; }

  /* Back */
  .card-back { padding: 26px 34px; }
  .appointment-title {
    font-size: 15px;
    font-weight: 700;
    letter-spacing: 0.5px;
    text-align: center;
  }
  .field-row {
    display: flex;
    align-items: flex-end;
    gap: 10px;
    margin-top: 20px;
    font-size: 14px;
    font-weight: 600;
  }
  .field-label { white-space: nowrap; }
  .field-line {
    flex: 1;
    border-bottom: 1.5px solid var(--line);
    height: 16px;
  }
  .check {
    display: inline-flex;
    align-items: center;
    gap: 5px;
    font-size: 13.5px;
    font-weight: 600;
  }
  .box {
    width: 17px; height: 12px;
    border: 1.5px solid var(--line);
    border-radius: 4px;
    display: inline-block;
  }
  .ampm { display: flex; gap: 10px; margin-left: 6px; }
  .days {
    display: flex;
    justify-content: space-between;
    margin-top: 26px;
  }
  .notice {
    position: absolute;
    left: 34px; right: 34px; bottom: 24px;
    font-size: 12.5px;
    line-height: 1.45;
    text-align: center;
    color: var(--ink);
  }
</style>
</head>
<body>

  <section class="card card-front" aria-label="Card front">
    <div class="smile-photo" role="img" aria-label="Close-up photograph of a smile with white teeth"></div>
    <div class="front-content">
      <div class="brand">
        <span class="brand-dot"></span>
        <span class="brand-name">Dental Lumora Clinic</span>
      </div>
      <p class="tagline">Harrowgate's home of dentistry</p>
      <p class="doctor">Dr Oswin Halvereth</p>
      <ul class="contact-list">
        <li>
          <svg viewBox="0 0 24 24"><path d="M6.6 10.8a15.1 15.1 0 0 0 6.6 6.6l2.2-2.2a1 1 0 0 1 1-.25 11.4 11.4 0 0 0 3.6.57 1 1 0 0 1 1 1V20a1 1 0 0 1-1 1A17 17 0 0 1 3 4a1 1 0 0 1 1-1h3.5a1 1 0 0 1 1 1c0 1.25.2 2.46.57 3.6a1 1 0 0 1-.25 1z"/></svg>
          <span>03 418 2276</span>
        </li>
        <li>
          <svg viewBox="0 0 24 24"><path d="M2 5h20v2l-10 7L2 7zM2 9l10 7 10-7v10H2z"/></svg>
          <span class="email">droswin@dentallumora.com</span>
        </li>
        <li>
          <svg viewBox="0 0 24 24"><circle cx="12" cy="12" r="10" fill="none" stroke="#2f4f84" stroke-width="2"/><path d="M2 12h20M12 2c3 3 3 17 0 20M12 2c-3 3-3 17 0 20" fill="none" stroke="#2f4f84" stroke-width="1.8"/></svg>
          <span>DentalLumoraClinic.com</span>
        </li>
        <li>
          <svg viewBox="0 0 24 24"><path d="M12 3l10 9h-3v9h-5v-6h-4v6H5v-9H2z"/></svg>
          <span class="address">47 Tallowmere Road Wrenfield<br>Northvale 4920</span>
        </li>
      </ul>
    </div>
  </section>

  <section class="card card-back" aria-label="Card back">
    <h2 class="appointment-title">APPOINTMENT</h2>
    <div class="field-row">
      <span class="field-label">Name:</span><span class="field-line"></span>
    </div>
    <div class="field-row">
      <span class="field-label">DATE:</span><span class="field-line"></span>
      <span class="field-label">TIME:</span><span class="field-line"></span>
      <span class="ampm">
        <span class="check">AM<span class="box"></span></span>
        <span class="check">PM<span class="box"></span></span>
      </span>
    </div>
    <div class="days">
      <span class="check">Mon<span class="box"></span></span>
      <span class="check">Tue<span class="box"></span></span>
      <span class="check">Wed<span class="box"></span></span>
      <span class="check">Thur<span class="box"></span></span>
      <span class="check">Fri<span class="box"></span></span>
      <span class="check">Sat<span class="box"></span></span>
    </div>
    <p class="notice">If unable to keep an appointment kindly give 24 hours notice<br>otherwise a fee will be charged for the time reserved</p>
  </section>

</body>
</html>
```